Business card design needed

the business is HR Consulting, but its for SME businesses who cant afford a permanent HR person. We sell an HR info system to help them meet minimum employment legislation but with this hope they then require us on a monthly subscription to phone or email us for HR advice. We are HR qualified mums working from home

So we will be partners to HR and Payroll systems known as unify HR and Tally

Target Market(s)

Small to medium businesses so not black and overly corporate, but having said that many are accounting businesses

Industry/Entity Type

Business

Contact Information for Business Card

Name of the company: Maple HR

Me:Marta Oldenbrook
Title:Managing Director

m: 0438 615 209
e: marta@maplehr.com.au
w: www.maplehr.com.au

What we do: HR Consulting, HR Systems and support, Payroll Advice

Requirements
Nice to have
• there is a company already out there known as Harbor professionals. I like the leaves at the end as I wanted something different like this to the usual business logos but still professional. I wanted a symbol to show calm, positive, ease flow going up ,etc. but realise they have the leaves and possibly cant copy, or can we?..( kite??, something calm and positive)dont know!!. Green and blue needed to be in it as nature and calm as well. I love the colours of www.staffingfundco.com ( attached the colours), as well as the calm wave line underneath. have a look as while they use green and blue I loved the purple colour thrown in there.Green and blue on their own are so overused. I want vibrant. I want double sided and when on a table I want it to stand out so maybe the purple colour (as per the colours on the fund website) solid on one side with just the 3 services we provide and personal and company name on front but need some creativity from you guys.

```html
<!DOCTYPE html>
<html lang="en">
<head>
<meta charset="utf-8">
<title>Maple HR – Business Card</title>
<link href="https://fonts.googleapis.com/css2?family=Saira:ital,wght@0,400;0,600;0,700;1,400&display=swap" rel="stylesheet">
<style>
  :root {
    --teal-light: #3bb3bd;
    --teal-deep: #15879a;
    --ink: #ffffff;
    --accent-plum: #9c3180;
    --divider: rgba(255, 255, 255, 0.85);
  }
  html, body {
    margin: 0;
    padding: 0;
    width: 1200px;
    height: 693px;
    overflow: hidden;
    background: #ffffff;
  }
  .card {
    position: relative;
    width: 1200px;
    height: 693px;
    background: linear-gradient(135deg, var(--teal-light) 0%, var(--teal-deep) 100%);
    color: var(--ink);
    font-family: "Saira", "Helvetica Neue", Arial, sans-serif;
    overflow: hidden;
  }
  .brand {
    position: absolute;
    left: 67px;
    top: 128px;
    width: 380px;
    text-align: center;
  }
  .brand-dot {
    display: block;
    width: 280px;
    height: 280px;
    margin: 0 auto;
    border-radius: 50%;
    background: var(--accent-plum);
  }
  .brand-name {
    margin: 24px 0 0;
    font-size: 64px;
    font-weight: 700;
    line-height: 1;
    letter-spacing: -0.5px;
  }
  .divider {
    position: absolute;
    left: 481px;
    top: 113px;
    width: 2px;
    height: 404px;
    background: var(--divider);
  }
  .person {
    position: absolute;
    left: 553px;
    top: 140px;
  }
  .person-name {
    margin: 0;
    font-size: 48px;
    font-weight: 600;
    line-height: 1.1;
  }
  .person-title {
    margin: 4px 0 0;
    font-size: 38px;
    font-style: italic;
    font-weight: 400;
    line-height: 1.1;
  }
  .contact-list {
    position: absolute;
    left: 553px;
    top: 305px;
    margin: 0;
    padding: 0;
    list-style: none;
  }
  .contact-item {
    display: flex;
    align-items: center;
    height: 56px;
    margin-bottom: 9px;
    font-size: 38px;
    font-weight: 400;
  }
  .contact-icon {
    width: 40px;
    height: 36px;
    margin-right: 22px;
    flex: none;
  }
  .services {
    position: absolute;
    left: 0;
    right: 0;
    top: 600px;
    margin: 0;
    text-align: center;
    font-size: 28px;
    font-weight: 400;
    letter-spacing: 3px;
  }
</style>
</head>
<body>
<main class="card">
  <section class="brand">
    <span class="brand-dot" aria-hidden="true"></span>
    <p class="brand-name">Maple HR</p>
  </section>

  <div class="divider" aria-hidden="true"></div>

  <section class="person">
    <h1 class="person-name">Marta Oldenbrook</h1>
    <p class="person-title">Managing Director</p>
  </section>

  <ul class="contact-list">
    <li class="contact-item">
      <svg class="contact-icon" viewBox="0 0 40 36" aria-hidden="true">
        <rect x="12" y="3" width="16" height="31" rx="3" fill="none" stroke="#fff" stroke-width="2.5"/>
        <rect x="15" y="7" width="10" height="8" fill="#fff"/>
        <g fill="#fff">
          <rect x="15" y="18" width="2.5" height="2.5"/><rect x="19" y="18" width="2.5" height="2.5"/><rect x="23" y="18" width="2.5" height="2.5"/>
          <rect x="15" y="22" width="2.5" height="2.5"/><rect x="19" y="22" width="2.5" height="2.5"/><rect x="23" y="22" width="2.5" height="2.5"/>
          <rect x="15" y="26" width="2.5" height="2.5"/><rect x="19" y="26" width="2.5" height="2.5"/><rect x="23" y="26" width="2.5" height="2.5"/>
        </g>
        <line x1="25" y1="3" x2="25" y2="0" stroke="#fff" stroke-width="2"/>
      </svg>
      <span>0438 615 209</span>
    </li>
    <li class="contact-item">
      <svg class="contact-icon" viewBox="0 0 40 36" aria-hidden="true">
        <rect x="2" y="7" width="36" height="22" fill="#fff"/>
        <polyline points="2,7 20,21 38,7" fill="none" stroke="#1f98a6" stroke-width="2"/>
        <line x1="2" y1="29" x2="15" y2="17" stroke="#1f98a6" stroke-width="1.5"/>
        <line x1="38" y1="29" x2="25" y2="17" stroke="#1f98a6" stroke-width="1.5"/>
      </svg>
      <span>marta@maplehr.com.au</span>
    </li>
    <li class="contact-item">
      <svg class="contact-icon" viewBox="0 0 40 36" aria-hidden="true">
        <g fill="none" stroke="#fff" stroke-width="2">
          <circle cx="20" cy="18" r="16"/>
          <ellipse cx="20" cy="18" rx="7" ry="16"/>
          <line x1="20" y1="2" x2="20" y2="34"/>
          <line x1="4" y1="18" x2="36" y2="18"/>
          <path d="M7 9 Q20 13 33 9"/>
          <path d="M7 27 Q20 23 33 27"/>
        </g>
      </svg>
      <span>www.maplehr.com.au</span>
    </li>
  </ul>

  <p class="services">HR Consulting , HR Systems and training , Payroll support</p>
</main>
</body>
</html>
```